Business Card Trio Design

We need a set of business cards that all match but are not identical. We need one generic for the business and one for each of the two owners. We would like the cards to be similar to each other, but not identical. We have a logo and the colors of the logo are painstakingly chosen so if blue or green is used, we prefer our specific blue and green. Our logo pops better on a black background as well. We are open to double-sided, but it is not the top choice. We would love some either gold or silver accents that are in a foiled appearance. We sell uniforms (scrubs, culinary, EMT, police, fire, business, all types except kids and sports), shoes, equipment, and accessories. We also have quorvalink, mavelgrid, lumopixel, and yondrel that we would like to have them follow and we offer zembrix in the store we would like the card to also advertise.

```html
<!DOCTYPE html>
<html lang="en">
<head>
<meta charset="utf-8">
<title>Norvale Workwear – Business Cards</title>
<link href="https://fonts.googleapis.com/css2?family=Cinzel:wght@500;600&family=Open+Sans:wght@400;600&display=swap" rel="stylesheet">
<style>
  :root {
    --brand-blue: #7ba7cf;
    --brand-green: #13a47f;
    --brand-green-deep: #0b8e6c;
    --card-black: #19191b;
    --card-ink: #eef0f2;
    --deco-ink: rgba(120, 140, 160, .12);
    --stage-light: #9a9a9c;
    --stage-dark: #6a6a6c;
    --serif: 'Cinzel', 'Times New Roman', serif;
    --sans: 'Open Sans', Arial, sans-serif;
  }
  * { box-sizing: border-box; margin: 0; padding: 0; }
  html, body { width: 1200px; height: 781px; overflow: hidden; }
  body {
    position: relative;
    background: radial-gradient(ellipse at 50% 40%, var(--stage-light) 0%, var(--stage-dark) 100%);
    font-family: var(--sans);
  }

  .card {
    position: absolute;
    top: 248px;
    width: 500px;
    height: 286px;
    border-radius: 18px;
    overflow: hidden;
    box-shadow: 0 18px 40px rgba(0, 0, 0, .35);
  }

  /* Contact side */
  .card--front { left: 70px; background: var(--card-black); }
  .card--front .deco-disc {
    position: absolute; right: -24px; top: 54px;
    width: 200px; height: 200px; border-radius: 50%;
    border: 28px solid var(--deco-ink);
  }
  .wordmark {
    position: absolute; left: 30px; top: 24px;
    display: flex; align-items: center; gap: 10px;
  }
  .wordmark__dot {
    width: 34px; height: 34px; border-radius: 50%;
    background: var(--brand-green);
    flex: none;
  }
  .wordmark__name {
    font-family: var(--serif); font-weight: 600;
    font-size: 20px; line-height: 1.05; letter-spacing: 2px;
    color: var(--brand-blue);
  }
  .holder { position: absolute; left: 30px; top: 90px; }
  .holder__name {
    font-family: var(--serif); font-weight: 500;
    font-size: 22px; letter-spacing: 1px; color: var(--brand-blue);
  }
  .holder__title { margin-top: 1px; font-size: 11px; color: var(--card-ink); }
  .rule {
    position: absolute; left: 30px; right: 60px; top: 140px;
    height: 1px; background: var(--brand-blue);
  }
  .contacts {
    position: absolute; left: 30px; top: 150px;
    list-style: none; font-size: 11.5px; color: var(--card-ink);
  }
  .contacts li { display: flex; align-items: center; gap: 7px; line-height: 19px; }
  .contacts svg { width: 10px; height: 10px; fill: var(--brand-green); flex: none; }
  .address {
    position: absolute; right: 60px; top: 196px;
    text-align: right; font-size: 12px; line-height: 18px; color: var(--card-ink);
  }
  .swoosh { position: absolute; left: 0; bottom: 0; width: 500px; height: 110px; }

  /* Brand side */
  .card--back {
    left: 630px;
    display: flex; align-items: center; justify-content: center;
    background: linear-gradient(135deg, #70a0c8 0%, #3fa7a4 45%, var(--brand-green-deep) 100%);
  }
  .card--back .deco-disc {
    position: absolute; right: 30px; top: 60px;
    width: 230px; height: 230px; border-radius: 50%;
    border: 30px solid rgba(255, 255, 255, .08);
  }
  .card--back .wordmark { position: relative; left: auto; top: auto; gap: 12px; }
  .card--back .wordmark__dot { width: 44px; height: 44px; background: #ffffff; }
  .card--back .wordmark__name { font-size: 28px; letter-spacing: 3px; color: #ffffff; }
</style>
</head>
<body>

<section class="card card--front" aria-label="Business card, contact side">
  <div class="deco-disc" aria-hidden="true"></div>
  <svg class="swoosh" viewBox="0 0 500 110" preserveAspectRatio="none" aria-hidden="true">
    <path d="M0 30 Q90 60 150 110 L0 110 Z" fill="var(--brand-blue)"/>
    <path d="M0 40 Q80 66 132 110 L0 110 Z" fill="var(--brand-green)"/>
  </svg>
  <div class="wordmark">
    <span class="wordmark__dot"></span>
    <span class="wordmark__name">Norvale<br>Workwear</span>
  </div>
  <div class="holder">
    <p class="holder__name">Dorian Pell</p>
    <p class="holder__title">President</p>
  </div>
  <div class="rule"></div>
  <ul class="contacts">
    <li><svg viewBox="0 0 10 10"><path d="M2 0.5 L3.6 2.6 L2.7 3.6 Q4 6 6.4 7.3 L7.4 6.4 L9.5 8 L8.4 9.5 Q1.5 8.5 0.5 1.6 Z"/></svg>(555) 214-7730</li>
    <li><svg viewBox="0 0 10 10"><path d="M0 2 H10 V8 H0 Z"/></svg>info@norvaleworkwear.com</li>
    <li><svg viewBox="0 0 10 10"><circle cx="5" cy="5" r="5"/></svg>www.norvaleworkwear.com</li>
  </ul>
  <p class="address">48 Brindle Market Plaza<br>Ashford Hollow, NC 27512</p>
</section>

<section class="card card--back" aria-label="Business card, brand side">
  <div class="deco-disc" aria-hidden="true"></div>
  <div class="wordmark">
    <span class="wordmark__dot"></span>
    <span class="wordmark__name">Norvale<br>Workwear</span>
  </div>
</section>

</body>
</html>
```